Business Cards for new orthopaedic surgery practice

My husband and I are starting our own orthopaedic surgery practice. We are looking for a business card that is uniform, but one will have my name/title and the other will have his. You can just create one design with my name on it for now. But when I choose your design as the winning design I will ask that you add another copy with his name/title.

We are looking for classy, simple, elite all in one. We like dark blues/a little gold/yellow. Something that goes with our logo. We want our logo incorporated. Here is all the info you need:
Business name: RV Spine & Vitality Center
Location: 38915 North Bramble Ave
Coral Springs, FL 33071
Phone: 954-218-4630
Fax: 954-571-2846
Email: info@myrvspine.example

Names: Lucinda Ferrow, M.D.
Board Certified Hand and Upper Extremity Surgeon

Emeka Dlunga, M.D.
Board Certified Hip & Knee Replacement/General Orthopaedic Surgeon

Can decide what you want to put on the back. Maybe a slogan:
Rooted in Care. Focused on You

I am just going to upload our logo. The only thing is if we select you as the winning design, the location, and phone numbers may change. We will need your help to update that once fully solidified.

Industry/Entity Type

Medical

Contact Information for Business Card

Colors
0054AA
0677BA
7BADD7
CADEEF
E8F1F8
0094D4
00A9DD
6FCCEA
C7EBF8
E9F6FB

Requirements
Must have
• class, appeal,
Should not have
• We want to air on the side of masculine if we are looking at masculine vs. feminine feel. But we still want it classy, sophisticated, and something we will love

```html
<!DOCTYPE html>
<html lang="en">
<head>
<meta charset="utf-8">
<title>RV Spine &amp; Vitality Center — Business Card</title>
<link rel="stylesheet" href="https://fonts.googleapis.com/css2?family=Cinzel:wght@400;500&family=Montserrat:wght@400;500;600;700&display=swap">
<style>
  :root {
    --page: #e8e8ea;
    --navy: #0f1d44;
    --navy-edge: #16275a;
    --gold: #c9a24a;
    --white: #ffffff;
    --soft: #d9deea;
  }
  * { margin: 0; padding: 0; box-sizing: border-box; }
  html, body { width: 800px; height: 1200px; overflow: hidden; }
  body {
    background: var(--page);
    font-family: "Montserrat", sans-serif;
    position: relative;
  }
  .card {
    position: absolute;
    left: 60px;
    width: 680px;
    height: 389px;
    background: var(--navy);
    box-shadow: 0 10px 28px rgba(15, 29, 68, 0.25);
    overflow: hidden;
  }
  .card--front { top: 181px; }
  .card--back { top: 630px; }

  .divider {
    position: absolute;
    left: 340px;
    top: 80px;
    width: 1.5px;
    height: 229px;
    background: var(--gold);
  }

  /* Front */
  .identity {
    position: absolute;
    left: 58px;
    top: 104px;
    width: 260px;
  }
  .identity__name {
    font-family: "Cinzel", serif;
    font-weight: 400;
    color: var(--gold);
    font-size: 38px;
    line-height: 1.12;
    letter-spacing: 1px;
  }
  .identity__rule {
    width: 160px;
    height: 1px;
    background: var(--gold);
    margin: 16px 0 14px;
  }
  .identity__title {
    color: var(--soft);
    font-size: 12.5px;
    font-weight: 500;
    line-height: 1.5;
    letter-spacing: 1.4px;
    text-transform: uppercase;
  }

  .contacts {
    position: absolute;
    left: 372px;
    top: 96px;
    list-style: none;
  }
  .contacts__item {
    display: flex;
    align-items: flex-start;
    gap: 14px;
    color: var(--white);
    font-size: 14px;
    line-height: 1.45;
    margin-bottom: 16px;
  }
  .contacts__icon {
    flex: 0 0 18px;
    width: 18px;
    height: 18px;
    margin-top: 1px;
  }

  /* Back */
  .brand {
    position: absolute;
    left: 44px;
    top: 154px;
    display: flex;
    align-items: center;
    gap: 16px;
  }
  .brand__mark {
    width: 72px;
    height: 72px;
    border: 2px solid var(--white);
    border-radius: 50%;
    flex: 0 0 72px;
  }
  .brand__name {
    color: var(--white);
    font-weight: 600;
    font-size: 16px;
    line-height: 1.35;
    letter-spacing: 1.5px;
    text-transform: uppercase;
  }

  .tagline {
    position: absolute;
    left: 376px;
    top: 108px;
    font-size: 31px;
    line-height: 1.2;
    letter-spacing: 1.5px;
    text-transform: uppercase;
    color: var(--white);
    font-weight: 500;
  }
  .tagline__accent {
    color: var(--gold);
    font-weight: 700;
    display: block;
  }
  .tagline__line { display: block; }
</style>
</head>
<body>

  <section class="card card--front" aria-label="Business card front">
    <div class="identity">
      <h1 class="identity__name">Lucinda<br>Ferrow, M.D.</h1>
      <div class="identity__rule"></div>
      <p class="identity__title">Board Certified<br>Hand &amp; Upper<br>Extremity Surgeon</p>
    </div>

    <div class="divider"></div>

    <ul class="contacts">
      <li class="contacts__item">
        <svg class="contacts__icon" viewBox="0 0 24 24" aria-hidden="true"><path d="M12 2a7 7 0 0 0-7 7c0 5.2 7 13 7 13s7-7.8 7-13a7 7 0 0 0-7-7zm0 9.5A2.5 2.5 0 1 1 12 6.5a2.5 2.5 0 0 1 0 5z" fill="#c9a24a"/></svg>
        <span>38915 North Bramble Ave<br>Coral Springs, FL 33071</span>
      </li>
      <li class="contacts__item">
        <svg class="contacts__icon" viewBox="0 0 24 24" aria-hidden="true"><path d="M6.6 10.8a15.1 15.1 0 0 0 6.6 6.6l2.2-2.2a1 1 0 0 1 1-.25 11.4 11.4 0 0 0 3.6.57 1 1 0 0 1 1 1V20a1 1 0 0 1-1 1A17 17 0 0 1 3 4a1 1 0 0 1 1-1h3.5a1 1 0 0 1 1 1c0 1.25.2 2.45.57 3.57a1 1 0 0 1-.25 1z" fill="#c9a24a"/></svg>
        <span>954-218-4630</span>
      </li>
      <li class="contacts__item">
        <svg class="contacts__icon" viewBox="0 0 24 24" aria-hidden="true"><path d="M7 3h8l3 3v4H7zM4 10h16a2 2 0 0 1 2 2v6h-4v3H6v-3H2v-6a2 2 0 0 1 2-2zm4 6v3h8v-3z" fill="#c9a24a"/></svg>
        <span>954-571-2846</span>
      </li>
      <li class="contacts__item">
        <svg class="contacts__icon" viewBox="0 0 24 24" aria-hidden="true"><path d="M3 5h18a1 1 0 0 1 1 1v12a1 1 0 0 1-1 1H3a1 1 0 0 1-1-1V6a1 1 0 0 1 1-1zm9 7.2L4.2 7v.1L12 12.4l7.8-5.3V7z" fill="#c9a24a"/></svg>
        <span>info@myrvspine.example</span>
      </li>
    </ul>
  </section>

  <section class="card card--back" aria-label="Business card back">
    <div class="brand">
      <div class="brand__mark"></div>
      <p class="brand__name">RV Spine &amp;<br>Vitality Center</p>
    </div>

    <div class="divider"></div>

    <p class="tagline">
      <span class="tagline__line">Rooted in</span>
      <span class="tagline__accent">Care</span>
      <span class="tagline__line">Focused on</span>
      <span class="tagline__accent">You</span>
    </p>
  </section>

</body>
</html>
```